Brisco Skiff Ferry and Haulage Business Card

I need business cards for my new water taxi and freight transport business I have started here in Kodiak Alaska. Kodiak is a remote island in the middle of the gulf of Alaska. There are seven native villages around the island and Kodiak is the #2 fishing port in the United States. We also have the largest Harbor Watch Base in the U.S. My company will be providing water taxi and freight transport logistics to the villages and many hunting and fishing lodges as well as remote properties around the island.

I would like a business card that isn't status quo, something that stands out, either in feel or appearance. I do like clean minimal designs but it needs to have the necessary contact info on it.

Target Market(s)

remote lodge / property owners, residents of the many villages around Kodiak and any one wanting to enjoy the great outdoors of Kodiak Alaska

Industry/Entity Type

Business

Contact Information for Business Card

I like clean simple designs that aren't cluttered but still provide the necessary information

Colors
0255a3
3277b5
33a4d5
9bcb3c
add136
fbed22
ffc214
f78f20
f37122

Requirements
Must have
• logo and contact info
• Captain Wade Pemberton
• www.briscoskiffferry.net
• wade@briscoskiffferry.net

```html
<!DOCTYPE html>
<html lang="en">
<head>
<meta charset="utf-8">
<title>Brisco Skiff Ferry and Haulage – Business Card</title>
<link rel="stylesheet" href="https://fonts.googleapis.com/css2?family=Open+Sans:wght@400;600;700&display=swap">
<style>
  :root {
    --navy: #0a3d8f;
    --royal: #0255a3;
    --mid-blue: #3277b5;
    --sky: #33a4d5;
    --orange: #f78f20;
    --amber: #ffc214;
    --ink-blue: #1f5fae;
    --paper: #ffffff;
    --backdrop: #e9ecef;
  }
  * { margin: 0; padding: 0; box-sizing: border-box; }
  html, body { width: 1200px; height: 913px; overflow: hidden; }
  body {
    background: var(--backdrop);
    font-family: "Open Sans", Arial, sans-serif;
    position: relative;
  }
  .card {
    position: absolute;
    width: 540px;
    height: 309px;
    overflow: hidden;
    box-shadow: 0 10px 24px rgba(0,0,0,0.18);
  }
  .card-front { left: 50px; top: 170px; background: var(--paper); }
  .card-back {
    left: 610px; top: 434px;
    background: linear-gradient(160deg, var(--mid-blue) 0%, var(--royal) 45%, var(--navy) 100%);
  }
  .card-shapes { position: absolute; inset: 0; }

  .brand-block {
    position: absolute;
    left: 34px; top: 92px;
    width: 190px;
    display: flex; align-items: center; gap: 10px;
  }
  .brand-dot {
    flex: none;
    width: 34px; height: 34px; border-radius: 50%;
    background: var(--sky);
  }
  .brand-name {
    font-weight: 700;
    font-size: 19px;
    line-height: 1.15;
    color: var(--royal);
  }
  .divider {
    position: absolute;
    left: 240px; top: 82px;
    width: 2px; height: 86px;
    background: var(--royal);
  }
  .contact {
    position: absolute;
    left: 258px; top: 84px;
    color: var(--ink-blue);
  }
  .contact-name {
    font-weight: 700;
    font-size: 19px;
    color: var(--mid-blue);
    margin-bottom: 10px;
  }
  .contact-line {
    display: flex; align-items: center; gap: 8px;
    font-size: 13px;
    line-height: 1.6;
  }
  .contact-line svg { flex: none; }

  .back-brand {
    position: absolute;
    left: 0; right: 0; top: 100px;
    text-align: center;
    font-weight: 700;
    font-size: 30px;
    line-height: 1.2;
    color: var(--paper);
  }
</style>
</head>
<body>

  <section class="card card-front" aria-label="Business card front">
    <svg class="card-shapes" viewBox="0 0 540 309" preserveAspectRatio="none" aria-hidden="true">
      <polygon points="0,300 540,262 540,309 0,309" fill="var(--royal)"/>
      <polygon points="250,309 262,258 540,200 540,309" fill="var(--sky)"/>
      <polygon points="250,309 262,258 540,200 540,216 270,272 260,309" fill="var(--mid-blue)" opacity="0.5"/>
    </svg>

    <div class="brand-block">
      <span class="brand-dot" aria-hidden="true"></span>
      <span class="brand-name">Brisco Skiff Ferry &amp; Haulage</span>
    </div>

    <div class="divider" aria-hidden="true"></div>

    <div class="contact">
      <p class="contact-name">Captain Wade Pemberton</p>
      <p class="contact-line">
        <svg width="12" height="10" viewBox="0 0 12 10" aria-hidden="true">
          <rect x="0.75" y="0.75" width="10.5" height="8.5" fill="none" stroke="var(--orange)" stroke-width="1.5"/>
          <polyline points="1,1 6,5.5 11,1" fill="none" stroke="var(--orange)" stroke-width="1.5"/>
        </svg>
        wade@briscoskiffferry.net
      </p>
      <p class="contact-line">
        <svg width="12" height="12" viewBox="0 0 12 12" aria-hidden="true">
          <circle cx="6" cy="6" r="5.2" fill="none" stroke="var(--orange)" stroke-width="1.4"/>
          <ellipse cx="6" cy="6" rx="2.4" ry="5.2" fill="none" stroke="var(--orange)" stroke-width="1.1"/>
          <line x1="0.8" y1="6" x2="11.2" y2="6" stroke="var(--orange)" stroke-width="1.1"/>
        </svg>
        www.briscoskiffferry.net
      </p>
    </div>
  </section>

  <section class="card card-back" aria-label="Business card back">
    <svg class="card-shapes" viewBox="0 0 540 309" preserveAspectRatio="none" aria-hidden="true">
      <polygon points="190,309 200,255 470,205 540,196 540,309" fill="var(--sky)"/>
      <polygon points="520,160 540,156 540,309 520,309" fill="var(--orange)"/>
      <polygon points="0,300 120,286 125,309 0,309" fill="var(--orange)"/>
    </svg>
    <p class="back-brand">Brisco Skiff<br>Ferry &amp; Haulage</p>
  </section>

</body>
</html>
```